Atelier Marrow Architecture business card

We need to update our business card. We do high end custom residential, hospitality, and wellness architecture. We focus on creating unique spaces and design around the five senses, believing that architecture's true impact is not on our surroundings, but within us. We would like to see designs are instill a sense of calm awe. They should be crisp, fresh, clean, authentic, & contemporary without being sterile, overworked, or harsh. White space is important. Alternative materials are an option if natural. We have created our own logo and would like designs to incorporate it. However, we are willing to see alternatives if the logo becomes a stumbling block and you have an alternate you suggest. Card must have the following information:
Atelier Marrow Architecture, Inc.
728 Holloway Ct. NE Atlanta, GA 30318
Marcus T. Whitcombe, AIA, NCARB, LEED AP BD+C
ateliermarrow.example

Target Market(s)

Higher net worth individuals with an appreciation for design, nature, sustainability,

Industry/Entity Type

Architect

Contact Information for Business Card

See above. The title of Owner or Architect is helpful but not necessary. Minimalism should trump additional information.

Font styles to use
Serif
Sans Serif

Requirements
Must have
• It should look professional. It must use logo
Should not have
• caligraphy, animals, anything that is cute,

```html
<!DOCTYPE html>
<html lang="en">
<head>
<meta charset="utf-8">
<title>Atelier Marrow Architecture — Business Card</title>
<link rel="stylesheet" href="https://fonts.googleapis.com/css2?family=Jost:wght@300;400;500&display=swap">
<style>
  :root {
    --stage: #2f2a2d;
    --card-white: #ffffff;
    --card-charcoal: #4a4a4c;
    --ink: #3d3d3f;
    --green: #0b5a3a;
    --crimson: #9b1b30;
    --rule: #c4c4c4;
    --white: #ffffff;
  }
  * { box-sizing: border-box; margin: 0; padding: 0; }
  html, body {
    width: 1200px; height: 1200px; overflow: hidden;
    background: var(--stage);
    font-family: "Jost", "Futura", sans-serif;
  }
  .card {
    position: absolute; left: 253px; width: 694px; height: 393px;
    border-radius: 19px; overflow: hidden;
  }
  .card--front { top: 183px; background: var(--card-white); }
  .card--back { top: 622px; background: var(--card-charcoal); }

  .front__margin-rule {
    position: absolute; left: 40px; top: 0; bottom: 0;
    width: 1.5px; background: var(--crimson);
  }
  .front__divider {
    position: absolute; left: 0; right: 0; top: 259px;
    height: 1.5px; background: var(--rule);
  }
  .wordmark {
    font-weight: 400; text-transform: uppercase; white-space: nowrap;
  }
  .front__wordmark {
    position: absolute; right: 36px; top: 64px;
    font-size: 17px; letter-spacing: 0.3em; color: var(--ink);
  }
  .front__person { position: absolute; left: 52px; top: 196px; }
  .person__name {
    font-size: 19px; font-weight: 500; color: var(--green); line-height: 24px;
  }
  .person__title {
    font-size: 19px; font-weight: 300; color: var(--crimson); line-height: 24px;
  }
  .contact-list {
    position: absolute; left: 52px; top: 272px; list-style: none;
  }
  .contact-list li {
    display: flex; align-items: center; gap: 10px;
    height: 23.5px; font-size: 19px; font-weight: 300; color: var(--ink);
  }
  .contact-list svg { width: 20px; height: 18px; flex: none; }
  .front__address {
    position: absolute; right: 27px; top: 295px; text-align: right;
    font-style: normal; font-size: 19px; font-weight: 300;
    line-height: 23.5px; color: var(--ink);
  }
  .back__wordmark {
    position: absolute; left: 40px; right: 40px; top: 176px; text-align: center;
    font-size: 22px; letter-spacing: 0.22em; color: var(--white);
    padding-left: 0.22em;
  }
</style>
</head>
<body>
  <section class="card card--front" aria-label="Business card front">
    <div class="front__margin-rule"></div>
    <p class="wordmark front__wordmark">Atelier Marrow Architecture</p>
    <div class="front__person">
      <p class="person__name">Marcus T. Whitcombe, AIA, NCARB, LEED AP BD+C</p>
      <p class="person__title">Architect</p>
    </div>
    <div class="front__divider"></div>
    <ul class="contact-list">
      <li>
        <svg viewBox="0 0 20 18" aria-hidden="true"><path fill="#0b5a3a" d="M1 6c0-3 4-4 9-4s9 1 9 4v2h-4V6c0-1-2-1.5-5-1.5S5 5 5 6v2H1z"/><path fill="#0b5a3a" d="M4 9h12l1 7H3z"/><circle cx="10" cy="12.5" r="2" fill="#fff"/></svg>
        555.014.2296
      </li>
      <li>
        <svg viewBox="0 0 20 18" aria-hidden="true"><rect x="5" y="1" width="10" height="5" fill="#0b5a3a"/><rect x="1" y="6" width="18" height="8" rx="1.5" fill="#0b5a3a"/><rect x="5" y="11" width="10" height="6" fill="#0b5a3a" stroke="#fff" stroke-width="1"/></svg>
        555.014.2297
      </li>
      <li>
        <svg viewBox="0 0 20 18" aria-hidden="true"><rect x="1" y="3" width="18" height="12" fill="#0b5a3a"/><path d="M1.5 3.5 10 10l8.5-6.5M1.5 14.5 8 8.5M18.5 14.5 12 8.5" fill="none" stroke="#fff" stroke-width="1.4"/></svg>
        info@ateliermarrow.example
      </li>
      <li>
        <svg viewBox="0 0 20 18" aria-hidden="true"><g fill="none" stroke="#0b5a3a" stroke-width="1.3"><circle cx="10" cy="9" r="8"/><ellipse cx="10" cy="9" rx="3.5" ry="8"/><path d="M2 9h16M3.2 5h13.6M3.2 13h13.6"/></g></svg>
        ateliermarrow.example
      </li>
    </ul>
    <address class="front__address">
      Atelier Marrow Architecture, Inc.<br>
      728 Holloway Ct. NE<br>
      Atlanta, GA 30318
    </address>
  </section>

  <section class="card card--back" aria-label="Business card back">
    <p class="wordmark back__wordmark">Atelier Marrow Architecture</p>
  </section>
</body>
</html>
```